Pizza Snack Pack Design

The design of sleeve for “Crunch Harbor” packs, this is a tray of cheese & pizza flavored snack bread.
Sleeve covers the tray and offers two circular windows on the sleeve to show the cheese and snack bread.
With this project we are looking to convey to consumer that he/she is having pizza snack.
This is for the convenience or “food to go” section of the stores.

We have the information that will be printed on the base of the pack including ingredients, pack weight, bar code etc. it is important for the designer to focus on the top and side panels.
There is no limit to the number of colors can be used as we will be printing full color.

Target Market(s)

Any pizza loving person, 12 years and above, office workers, travelers, university students
Convenience stores, shops at airports, train stations, petrol stations.

Industry/Entity Type

Printing

Font styles to use
Serif
Sans Serif
Decorative
Script

Requirements
Must have
• Design for the sleeve on tray containing dip & snack bread that offers two windows to show the contents.
• The sleeve dimension The width is 158mm and Height is 181mm that includes 20mm overlap.
• The tray dimension: L: 160mm W: 75mm H: 27mm.
• Note: The design is more important than getting the dimension correct. All emphasis should be on the top and side panels. We will add the content details in-house.
Nice to have
• Strong emphasis on pizza flavor of the snack pack.
• Re-design of the pack name i.e. the Crunch Harbor writing to suit the new design.
Should not have
• Avoid clatter of shapes and writing and color clash.
• The design must tell the content within 10 second of consumer looking at it.

```html
<!DOCTYPE html>
<html lang="en">
<head>
<meta charset="utf-8">
<title>Crunch Harbor – Snack Pack Sleeve</title>
<link href="https://fonts.googleapis.com/css2?family=Sansita:ital,wght@1,800&family=Delius&family=Raleway:wght@600;700&display=swap" rel="stylesheet">
<style>
  :root {
    --bg: #ece8e2;
    --brown: #4a2610;
    --brown-dark: #341a09;
    --beige: #e3cfae;
    --leaf: #7fb03a;
    --leaf-dark: #5e8c26;
    --blur-warm: #c9ab86;
    --blur-light: #f1ebe2;
    --ink: #2f1c0e;
    --mark: #1f6b2c;
  }
  * { margin: 0; padding: 0; box-sizing: border-box; }
  html, body { width: 1200px; height: 900px; overflow: hidden; background: var(--bg); }
  .canvas { position: relative; width: 1200px; height: 900px; }

  .sleeve { position: absolute; left: 85px; top: 180px; width: 1030px; height: 528px; }

  .top-panel {
    position: absolute; left: 0; top: 0; width: 1030px; height: 368px;
    border-top: 3px solid var(--leaf);
    overflow: hidden;
  }
  .backdrop-photo {
    position: absolute; inset: 0;
    background:
      radial-gradient(ellipse 320px 170px at 520px 150px, var(--blur-light) 0%, rgba(241,235,226,0) 100%),
      radial-gradient(ellipse 280px 150px at 900px 330px, #d9a36a 0%, rgba(217,163,106,0) 100%),
      radial-gradient(ellipse 160px 200px at 40px 320px, #8aa45a 0%, rgba(138,164,90,0) 100%),
      linear-gradient(180deg, #ddd0bf 0%, var(--blur-warm) 60%, #c09a70 100%);
  }
  .panel-art { position: absolute; left: 0; top: 0; }

  .name-banner { position: absolute; left: 395px; top: 0; width: 262px; height: 96px; }
  .name-banner svg { position: absolute; left: 0; top: 0; }
  .name-banner .banner-text {
    position: absolute; inset: 0; padding-top: 4px;
    font-family: "Sansita", sans-serif; font-style: italic; font-weight: 800;
    color: var(--beige); text-align: center; line-height: 38px; font-size: 35px;
  }

  .net-weight {
    position: absolute; right: 14px; top: 322px;
    font-family: "Raleway", sans-serif; font-weight: 700; color: var(--ink);
    font-size: 15px;
  }
  .net-weight b { font-size: 24px; margin-left: 6px; }

  .side-panel {
    position: absolute; left: 0; top: 368px; width: 1030px; height: 160px;
    background: linear-gradient(180deg, var(--brown) 0%, var(--brown-dark) 100%);
    border-top: 6px solid var(--leaf);
  }
  .maker {
    position: absolute; left: 47px; top: 12px;
    display: flex; align-items: center; gap: 6px;
    font-family: "Raleway", sans-serif; font-weight: 600; font-size: 13px; color: var(--beige);
  }
  .maker .mark { width: 18px; height: 18px; background: var(--mark); }
  .brand-title {
    position: absolute; left: 0; right: 0; top: 16px; text-align: center;
    font-family: "Sansita", sans-serif; font-style: italic; font-weight: 800;
    font-size: 64px; line-height: 76px; color: var(--beige);
    -webkit-text-stroke: 2px var(--leaf-dark); paint-order: stroke fill;
    text-shadow: 2px 3px 0 var(--leaf-dark);
    padding-left: 20px;
  }
  .tagline {
    position: absolute; left: 0; right: 0; top: 102px; text-align: center;
    font-family: "Delius", sans-serif; font-size: 33px; color: var(--leaf);
    padding-left: 20px; letter-spacing: 1px;
  }
</style>
</head>
<body>
<main class="canvas">
  <section class="sleeve">
    <div class="top-panel">
      <div class="backdrop-photo" role="img" aria-label="Soft-focus photo of pizza-flavoured snack bread with creamy cheese dip"></div>

      <svg class="panel-art" width="1030" height="368" viewBox="0 0 1030 368">
        <defs>
          <path id="wave-frame" d="M1 0 Q1.063 .285 .866 .5 Q.778 .778 .5 .866 Q.285 1.063 0 1 Q-.285 1.063 -.5 .866 Q-.778 .778 -.866 .5 Q-1.063 .285 -1 0 Q-1.063 -.285 -.866 -.5 Q-.778 -.778 -.5 -.866 Q-.285 -1.063 0 -1 Q.285 -1.063 .5 -.866 Q.778 -.778 .866 -.5 Q1.063 -.285 1 0Z"/>
          <radialGradient id="dip-tones" cx="0.5" cy="0.45" r="0.6">
            <stop offset="0" stop-color="#e6e2de"/>
            <stop offset="0.6" stop-color="#d9d3cc"/>
            <stop offset="1" stop-color="#b9584a"/>
          </radialGradient>
          <radialGradient id="bread-tones" cx="0.45" cy="0.45" r="0.6">
            <stop offset="0" stop-color="#ddd3b8"/>
            <stop offset="0.7" stop-color="#cbbf9c"/>
            <stop offset="1" stop-color="#a88f62"/>
          </radialGradient>
          <radialGradient id="serving-tones" cx="0.5" cy="0.35" r="0.6">
            <stop offset="0" stop-color="#f3ede1"/>
            <stop offset="0.45" stop-color="#e8dcc3"/>
            <stop offset="0.75" stop-color="#c98a4c"/>
            <stop offset="1" stop-color="#b0442e"/>
          </radialGradient>
        </defs>

        <g class="window window-dip">
          <use href="#wave-frame" transform="translate(250 168) scale(142 128)" fill="var(--leaf)"/>
          <use href="#wave-frame" transform="translate(250 168) scale(135 121)" fill="#ffffff"/>
          <use href="#wave-frame" transform="translate(256 166) scale(124 110)" fill="url(#dip-tones)" role="img" aria-label="Cheese dip tub with its label visible through the window"/>
        </g>

        <g class="window window-bread">
          <use href="#wave-frame" transform="translate(800 168) scale(152 128)" fill="var(--leaf)"/>
          <use href="#wave-frame" transform="translate(800 168) scale(145 121)" fill="#ffffff"/>
          <use href="#wave-frame" transform="translate(796 170) scale(134 110)" fill="url(#bread-tones)" role="img" aria-label="Pizza-flavoured snack bread slices visible through the window"/>
        </g>

        <g class="serving">
          <ellipse cx="518" cy="314" rx="172" ry="40" fill="#9a8a4a" opacity="0.55"/>
          <ellipse cx="518" cy="306" rx="138" ry="30" fill="#6f8f2a"/>
          <ellipse cx="520" cy="258" rx="114" ry="78" fill="url(#serving-tones)" role="img" aria-label="Toasted pizza-flavoured bread slice topped with cheese spread and a herb leaf"/>
        </g>
      </svg>

      <div class="name-banner">
        <svg width="262" height="96" viewBox="0 0 262 96">
          <path d="M0 0 H262 V90 Q196 78 131 86 Q66 94 0 84 Z" fill="var(--brown)"/>
          <path d="M0 84 Q66 94 131 86 Q196 78 262 90" fill="none" stroke="var(--leaf)" stroke-width="3"/>
        </svg>
        <div class="banner-text">Crunch<br>Harbor</div>
      </div>

      <div class="net-weight">Net weight:<b>40g</b></div>
    </div>

    <div class="side-panel">
      <div class="maker"><span class="mark"></span>Brightleaf Foods</div>
      <h1 class="brand-title">Crunch Harbor</h1>
      <p class="tagline">a tasty snack for any time of the day</p>
    </div>
  </section>
</main>
</body>
</html>
```